Public Speaking Book for aspiring, ambitious speakers

I'm looking for a 6x9 book cover (Parcelo standard) as well as ebook and audiobook formats.

I'm looking for orange font on a white background as these are my brand colours.

Feel free to use some yellow and gold too if you deem it appropriate.

Title: Climb and Glow
Subtitle: Find Your Voice. Tell Your Story. Share your Message.
Author: Lionel Barstow

I would like to have a picture of a female speaker on the front cover.

Alternatively, some kind of image that symbolises public speaking like a microphone, podium etc

Target Market(s)

Aspiring professional speakers

Colors
f78f20

Requirements
Must have
• Correct spelling!
Nice to have
• A logo or picture that fits the theme, but no pressure if you can't think of anything
Should not have
• No men in suits please. I don't want this to have a 1980s corporate look.

```html
<!DOCTYPE html>
<html lang="en">
<head>
<meta charset="utf-8">
<title>Climb and Glow — Lionel Barstow</title>
<link href="https://fonts.googleapis.com/css2?family=Montserrat:wght@300;500;600;700&display=swap" rel="stylesheet">
<style>
  :root {
    --brand-orange: #f78f20;
    --ink: #1c1c1c;
    --paper: #ffffff;
    --peach: #fbd6a4;
    --photo-warm: #e9a25a;
    --photo-deep: #8a4a22;
    --white: #ffffff;
  }
  * { margin: 0; padding: 0; box-sizing: border-box; }
  html, body { width: 802px; height: 1200px; overflow: hidden; }
  body { font-family: "Montserrat", Arial, sans-serif; background: var(--paper); }

  .cover {
    position: relative;
    width: 802px;
    height: 1200px;
    overflow: hidden;
    background:
      radial-gradient(ellipse 720px 560px at 0% 78%, var(--peach) 0%, rgba(251,214,164,0.55) 45%, rgba(255,255,255,0) 80%),
      radial-gradient(ellipse 900px 700px at 60% 95%, #fde2bc 0%, rgba(255,255,255,0) 75%),
      var(--paper);
  }

  .title { position: absolute; left: 0; width: 100%; text-align: center; color: var(--brand-orange); line-height: 1; }
  .title-top { top: 44px; font-weight: 600; font-size: 186px; letter-spacing: -4px; }
  .title-joiner { top: 170px; font-weight: 300; font-size: 122px; letter-spacing: -2px; left: 30px; }
  .title-bottom { top: 266px; font-weight: 600; font-size: 186px; letter-spacing: -4px; }

  .subtitle { position: absolute; left: 46px; top: 492px; }
  .subtitle-line { margin-bottom: 26px; }
  .subtitle-lead { display: block; font-weight: 500; font-size: 28px; color: var(--ink); line-height: 34px; }
  .subtitle-key { display: block; font-weight: 700; font-size: 41px; color: var(--brand-orange); line-height: 48px; }

  .speaker-photo {
    position: absolute;
    left: 352px; top: 464px;
    width: 450px; height: 636px;
    border-radius: 48% 40% 0 0 / 30% 26% 0 0;
    background:
      radial-gradient(ellipse 150px 200px at 42% 42%, #f4b06a 0%, rgba(244,176,106,0) 100%),
      linear-gradient(180deg, var(--photo-deep) 0%, var(--photo-warm) 45%, #7b3f1c 80%, #2a2320 100%);
  }
  .mic-photo {
    position: absolute;
    left: 236px; top: 876px;
    width: 90px; height: 224px;
    border-radius: 40px 40px 14px 14px;
    background: linear-gradient(180deg, #9c9c9c 0%, #6b6b6b 28%, #2a2a2a 32%, #1b1b1b 100%);
  }

  .author-band {
    position: absolute; left: 0; top: 1100px;
    width: 802px; height: 100px;
    background: var(--brand-orange);
    display: flex; align-items: center; justify-content: center;
  }
  .author-name {
    color: var(--white);
    font-weight: 600;
    font-size: 40px;
    letter-spacing: 10px;
    padding-left: 10px;
    text-transform: uppercase;
  }
</style>
</head>
<body>
  <main class="cover">
    <h1 class="book-title">
      <span class="title title-top">CLIMB</span>
      <span class="title title-joiner">and</span>
      <span class="title title-bottom">GLOW</span>
    </h1>

    <div class="subtitle">
      <p class="subtitle-line"><span class="subtitle-lead">Find Your</span><span class="subtitle-key">VOICE</span></p>
      <p class="subtitle-line"><span class="subtitle-lead">Tell Your</span><span class="subtitle-key">STORY</span></p>
      <p class="subtitle-line"><span class="subtitle-lead">Share your</span><span class="subtitle-key">MESSAGE</span></p>
    </div>

    <div class="speaker-photo" role="img" aria-label="Photo of a smiling female speaker with long auburn hair, looking up and to the left"></div>
    <div class="mic-photo" role="img" aria-label="Photo of a handheld microphone held by the speaker"></div>

    <footer class="author-band">
      <p class="author-name">Lionel Barstow</p>
    </footer>
  </main>
</body>
</html>
```